New Business Card Design Project

We are looking for a talented individual to create a truly awesome/unique business card design for us. We are looking for a someone to design something that will really stand out from the crowd - we don't mind what ideas you come up with (ie embossed/flat/matte/shine etc etc) just wow us with your creativity.
Updates

Target Market(s)

Video Games Industry Professionals (all levels of seniority from QA Testers through to CEOs)

Contact Information for Business Card

Company logo (see upload)
Company name: Northbay Play Careers Ltd
Employee Name: Darren Elsby
Job title: CEO
Website: www.nbpc2go.example
Office +44 1632 960418
Mobile: +44 7700 900276
Email: darren@nbpc2go.example

Colors

Designer to choose colors to be used in the design.

Requirements
Must have
• The business card design MUST contain all the information listed in the BUSINESS CARD DETAILS box.
• You will see the colours that are relevant to us (ie company logo) in the uploaded imagery - however you do not have to use all these colours when designing the business card itself
• MUST BE DOUBLE SIDED

```html
<!DOCTYPE html>
<html lang="en">
<head>
<meta charset="utf-8">
<title>Northbay Play Careers – Business Card</title>
<link rel="stylesheet" href="https://fonts.googleapis.com/css2?family=Lato:wght@400;700&display=swap">
<style>
  :root {
    --navy: #343a62;
    --orange: #ee7422;
    --white: #ffffff;
    --stage: #3a3a3a;
  }
  * { box-sizing: border-box; margin: 0; padding: 0; }
  html, body {
    width: 1200px; height: 912px; overflow: hidden;
    background: var(--stage);
    font-family: "Lato", Arial, sans-serif;
  }
  .card {
    position: absolute;
    width: 640px; height: 380px;
    overflow: hidden;
    box-shadow: 0 10px 30px rgba(0,0,0,.45);
  }
  .card-front { left: 70px; top: 60px; background: var(--navy); }
  .card-back  { left: 490px; top: 470px; background: var(--white); }

  .brand { position: absolute; display: flex; align-items: center; gap: 18px; }
  .brand-mark { width: 92px; height: 92px; border-radius: 50%; flex: none; }
  .brand-name { font-weight: 700; font-size: 34px; line-height: 1.05; }

  .card-front .brand { left: 110px; top: 130px; }
  .card-front .brand-mark { background: var(--white); }
  .card-front .brand-name { color: var(--white); }
  .card-front .website {
    position: absolute; left: 0; right: 0; top: 290px;
    text-align: center; color: var(--white); font-size: 17px; letter-spacing: .5px;
  }

  .back-shapes { position: absolute; inset: 0; }
  .card-back .brand { left: 36px; top: 34px; }
  .card-back .brand-mark { width: 70px; height: 70px; background: var(--navy); }
  .card-back .brand-name { color: var(--navy); font-size: 27px; }

  .person { position: absolute; right: 40px; top: 112px; text-align: right; color: var(--white); }
  .person-name { font-size: 20px; font-weight: 700; }
  .person-title { font-size: 15px; margin-top: 2px; }

  .contacts { position: absolute; left: 36px; top: 228px; color: var(--white); font-size: 15px; }
  .contact-row { display: flex; align-items: center; gap: 10px; line-height: 24px; }
  .contact-row svg { width: 15px; height: 15px; flex: none; }
  .company { margin-top: 12px; font-size: 15px; }

  .card-back .website {
    position: absolute; right: 40px; top: 252px;
    color: var(--navy); font-size: 15px;
  }
</style>
</head>
<body>

<section class="card card-front" aria-label="Card front">
  <div class="brand">
    <span class="brand-mark"></span>
    <span class="brand-name">Northbay Play<br>Careers</span>
  </div>
  <p class="website">www.nbpc2go.example</p>
</section>

<section class="card card-back" aria-label="Card back">
  <svg class="back-shapes" viewBox="0 0 640 380" preserveAspectRatio="none" aria-hidden="true">
    <path d="M0,205 C220,195 470,120 640,25 L640,220 C430,250 250,320 140,380 L0,380 Z" fill="var(--navy)"/>
    <path d="M120,190 C330,175 500,110 640,18" fill="none" stroke="var(--orange)" stroke-width="6"/>
    <path d="M130,380 C250,310 440,245 620,215" fill="none" stroke="var(--orange)" stroke-width="3"/>
    <path d="M0,380 L0,368 C80,365 140,355 200,340 C170,355 150,368 140,380 Z" fill="var(--orange)"/>
  </svg>

  <div class="brand">
    <span class="brand-mark"></span>
    <span class="brand-name">Northbay Play<br>Careers</span>
  </div>

  <div class="person">
    <p class="person-name">Darren Elsby</p>
    <p class="person-title">CEO</p>
  </div>

  <div class="contacts">
    <p class="contact-row">
      <svg viewBox="0 0 16 16"><path d="M4 1l3 3-2 2c1 2 3 4 5 5l2-2 3 3-2 3C7 15 1 9 1 4z" fill="var(--white)"/></svg>
      +44 1632 960418
    </p>
    <p class="contact-row">
      <svg viewBox="0 0 16 16"><rect x="4" y="1" width="8" height="14" rx="1.5" fill="none" stroke="var(--white)" stroke-width="1.6"/><circle cx="8" cy="12.5" r="1" fill="var(--white)"/></svg>
      +44 7700 900276
    </p>
    <p class="contact-row">
      <svg viewBox="0 0 16 16"><rect x="1" y="3" width="14" height="10" fill="none" stroke="var(--white)" stroke-width="1.6"/><path d="M1 3l7 6 7-6" fill="none" stroke="var(--white)" stroke-width="1.6"/></svg>
      darren@nbpc2go.example
    </p>
    <p class="company">Northbay Play Careers Ltd</p>
  </div>

  <p class="website">www.nbpc2go.example</p>
</section>

</body>
</html>
```